Business Card Design

Professional solutions in (servers, security, networks, programming)

Industry/Entity Type

Business

Contact Information for Business Card

Tarek Hounayni
Internet services and network solutions
DPV - RTLK - RTLB
netcare@qo-lam.com / 05917406238
www.qo-lam.com

```html
<!DOCTYPE html>
<html lang="en">
<head>
<meta charset="utf-8">
<title>Tarek Hounayni — Business Card</title>
<link rel="stylesheet" href="https://fonts.googleapis.com/css2?family=Tinos:wght@400;700&display=swap">
<style>
  :root {
    --page-bg: #d6d1c9;
    --card-blue-light: #3b5aa6;
    --card-blue-mid: #223a78;
    --card-navy: #0b1430;
    --band-fill: #b9bbd6;
    --band-text: #16204a;
    --text-white: #ffffff;
    --text-soft: #e4e8f4;
    --data-glow: rgba(190, 205, 240, 0.35);
  }

  * { margin: 0; padding: 0; box-sizing: border-box; }

  html, body {
    width: 1200px;
    height: 900px;
    overflow: hidden;
  }

  body {
    background: var(--page-bg);
    font-family: "Tinos", "Times New Roman", serif;
    position: relative;
  }

  .business-card {
    position: absolute;
    left: 100px;
    top: 164px;
    width: 1000px;
    height: 572px;
    overflow: hidden;
    background:
      radial-gradient(ellipse 70% 90% at 30% 40%, var(--card-blue-light) 0%, var(--card-blue-mid) 45%, var(--card-navy) 100%);
    box-shadow: 0 18px 40px rgba(0, 0, 0, 0.35);
  }

  .data-stream {
    position: absolute;
    right: 0;
    top: 0;
    width: 560px;
    height: 100%;
    background:
      linear-gradient(100deg, rgba(11, 20, 48, 0) 0%, var(--data-glow) 55%, rgba(230, 236, 250, 0.55) 100%);
    -webkit-mask-image: linear-gradient(90deg, transparent 0%, #000 40%);
            mask-image: linear-gradient(90deg, transparent 0%, #000 40%);
  }

  .identity {
    position: absolute;
    left: 88px;
    top: 150px;
    color: var(--text-white);
  }

  .identity__name {
    font-size: 54px;
    font-weight: 700;
    letter-spacing: 1px;
    line-height: 1;
  }

  .identity__credentials {
    font-size: 18px;
    font-weight: 400;
    letter-spacing: 1px;
    color: var(--text-soft);
    margin-top: 6px;
  }

  .contact {
    position: absolute;
    left: 90px;
    top: 262px;
    color: var(--text-white);
    line-height: 1.3;
  }

  .contact__phone {
    font-size: 30px;
    font-weight: 700;
    letter-spacing: 1px;
  }

  .contact__email,
  .contact__web {
    font-size: 26px;
    font-weight: 400;
    letter-spacing: 0.5px;
    color: var(--text-soft);
  }

  .services-band {
    position: absolute;
    left: 0;
    top: 406px;
    width: 100%;
    height: 48px;
    background: var(--band-fill);
    display: flex;
    align-items: center;
    padding-left: 270px;
  }

  .services-band__list {
    font-size: 31px;
    font-weight: 700;
    color: var(--band-text);
    letter-spacing: 0.5px;
    white-space: nowrap;
  }
</style>
</head>
<body>
  <article class="business-card">
    <div class="data-stream" role="img" aria-label="Binary digit stream receding into the distance"></div>

    <header class="identity">
      <h1 class="identity__name">Tarek Hounayni</h1>
      <p class="identity__credentials">DPV - RTLK - RTLB</p>
    </header>

    <address class="contact" style="font-style: normal;">
      <div class="contact__phone">05917406238</div>
      <div class="contact__email">netcare@qo-lam.com</div>
      <div class="contact__web">www.qo-lam.com</div>
    </address>

    <div class="services-band">
      <p class="services-band__list">Servers | Security | Networks | Programming</p>
    </div>
  </article>
</body>
</html>
```